Business Card Design

I need a business card for my rental business. The business is named:
Hire a Vorlatrike Brenmoor
www.hireavorlatrikebrenmoor.example
(555) 014-2937
This will be a business card that I will leave at other businesses as advertisement so it needs to have the name, website, and phone number.
Please feel free to be creative. This is a new business so I have no designs.
Thank you very much for your time and I look forward to receiving your designs
Target Market(s)
Local rental customers
Industry/Entity Type
Business
Contact Information for Business Card
Please check out my website:
Other font styles liked:
- anything creative
Colors
Designer to choose colors to be used in the design.
Requirements
Must have
- Business name, phone, website. Rentals available hourly or daily. Book online

```html
<!DOCTYPE html>
<html lang="en">
<head>
<meta charset="utf-8">
<title>Brenmoor Vorlatrike Rental – Business Card</title>
<link href="https://fonts.googleapis.com/css2?family=Tinos:wght@400;700&display=swap" rel="stylesheet">
<style>
  :root {
    --bg: #3b3b3b;
    --red: #d4232a;
    --black: #0c0c0c;
    --white: #ffffff;
    --ink: #111111;
  }
  * { margin: 0; padding: 0; box-sizing: border-box; }
  html, body { width: 1200px; height: 960px; overflow: hidden; background: var(--bg); }
  body { position: relative; font-family: "Tinos", "Times New Roman", serif; }

  .card {
    position: absolute;
    left: 250px;
    width: 700px;
    height: 400px;
    overflow: hidden;
    box-shadow: 0 10px 30px rgba(0,0,0,.45);
  }

  /* Front side */
  .card-front { top: 50px; background: var(--white); }
  .front-field {
    position: absolute; left: 0; top: 0; bottom: 0; width: 330px;
    background: var(--red);
  }
  .front-name {
    position: absolute; right: 40px; top: 140px;
    font-weight: 700; color: var(--ink);
    text-transform: uppercase; line-height: 1.05;
    text-align: right; white-space: nowrap;
  }
  .front-name .small { font-size: 22px; display: block; }
  .front-name .large { font-size: 42px; display: block; }

  /* Back side */
  .card-back { top: 510px; background: var(--black); }
  .back-band {
    position: absolute; left: 0; top: 0; width: 100%; height: 120px;
    background: var(--white);
    border-bottom: 4px solid var(--red);
  }
  .back-band::before {
    content: ""; position: absolute; left: 0; right: 0; top: 12px; height: 5px;
    background: var(--red);
  }
  .back-name {
    position: absolute; left: 150px; top: 32px;
    font-weight: 700; color: var(--ink); text-transform: uppercase;
    line-height: 1; text-align: right; white-space: nowrap;
  }
  .back-name .small { font-size: 18px; display: block; }
  .back-name .large { font-size: 40px; display: block; }

  .info-stack { position: absolute; left: 70px; top: 126px; width: 440px; }
  .info-bar {
    display: flex; align-items: center; justify-content: center;
    background: var(--red); color: var(--white);
    border: 2px solid var(--black);
    height: 44px; margin-bottom: 5px;
    font-size: 21px; letter-spacing: .5px; white-space: nowrap;
  }
  .info-bar.headline { height: 54px; color: var(--ink); font-weight: 700; font-size: 26px; }
  .info-bar.web { font-size: 19px; }
  .info-bar:nth-child(2) { margin-left: 10px; }
  .info-bar:nth-child(3) { margin-right: 10px; }
  .info-bar:nth-child(4) { margin-left: 14px; }
  .info-bar:nth-child(5) { margin-right: 14px; }
</style>
</head>
<body>
  <section class="card card-front" aria-label="Card front">
    <div class="front-field"></div>
    <div class="front-name">
      <span class="small">Brenmoor</span>
      <span class="large">Vorlatrike</span>
      <span class="small">Rental</span>
    </div>
  </section>

  <section class="card card-back" aria-label="Card back">
    <div class="back-band">
      <div class="back-name">
        <span class="small">Brenmoor</span>
        <span class="large">Vorlatrike</span>
        <span class="small">Rental</span>
      </div>
    </div>
    <div class="info-stack">
      <div class="info-bar headline">Hire a Vorlatrike Brenmoor</div>
      <div class="info-bar">(555) 014-2937</div>
      <div class="info-bar web">www.hireavorlatrikebrenmoor.example</div>
      <div class="info-bar">1 - 3 Days Rental</div>
      <div class="info-bar">Book Online NOw!!!</div>
    </div>
  </section>
</body>
</html>
```